Business Card- Occupational Therapist

I need business cards for Tallowood KinderMove, I am an Occupational Therapist offering child centred play therapy.
I am a sole private practitioner offering play therapy services to families in rural Great Southern region of WA, my mission statement is "helping rural children and communities thrive"
This is a new business so I am needing to promote the value of child centred play therapy within the community, and my referrers (target audience) will be: rural GPs (doctors), child health nurse, schools, disability providers, child protection workers etc) but also the families of young children in rural areas.
Target Market(s)
Families of children
Referrers (Doctors, child health nurse, schools, disability providers, child protection workers)
Industry/Entity Type
Mental Health
Contact Information for Business Card
Mira Toveland
Occupational Therapist
Phone: 0487 552 019
Email: mira@tkmove.com.au
PO Box 71 | BRELLAGUP WA 6388
Requirements
Must have
- Include Tallowood KinderMove logo and my contact details.
Include my credentials as an Occupational Therapist and Child Centred Play Therapist
Nice to have
- "Play is a child's language and toys are their words" Delbert Quorin

```html
<!DOCTYPE html>
<html lang="en">
<head>
<meta charset="utf-8">
<title>Tallowood KinderMove – Business Card</title>
<link rel="stylesheet" href="https://fonts.googleapis.com/css2?family=Comfortaa:wght@400&family=Roboto:wght@400;500&display=swap">
<style>
  :root {
    --backdrop: #2e2e2e;
    --purple: #6a1b63;
    --purple-deep: #5a1858;
    --green: #2a8f2f;
    --green-bright: #23992b;
    --card-white: #efefef;
    --ink: #1e1e1e;
    --soft-white: #ececec;
  }
  * { margin: 0; padding: 0; box-sizing: border-box; }
  html, body {
    width: 1200px; height: 1138px; overflow: hidden;
    background: var(--backdrop);
  }
  .card {
    position: absolute;
    border-radius: 16px;
    overflow: hidden;
  }
  .card-front {
    left: 274px; top: 186px; width: 623px; height: 376px;
    background:
      linear-gradient(180deg, rgba(0,0,0,0) 55%, rgba(0,0,0,0.12) 100%),
      linear-gradient(100deg, var(--purple-deep) 0%, #5a2a5a 28%, #4f4a52 48%, #3f6244 66%, var(--green-bright) 100%);
  }
  .front-name {
    position: absolute; left: 0; right: 0; top: 128px;
    text-align: center;
    font-family: 'Comfortaa', sans-serif;
    font-weight: 400;
    font-size: 50px; line-height: 56px;
    color: var(--soft-white);
  }
  .front-tagline {
    position: absolute; left: 0; right: 0; top: 340px;
    display: flex; align-items: center; justify-content: center; gap: 12px;
    font-family: 'Roboto', sans-serif; font-size: 16px;
    color: #e4e4e4;
  }
  .front-tagline .rule {
    width: 56px; height: 1.5px; background: #e4e4e4;
  }
  .card-back {
    left: 276px; top: 608px; width: 618px; height: 374px;
    background: linear-gradient(180deg, #f3f3f3 0%, var(--card-white) 60%, #e6e6e6 100%);
  }
  .edge-accent { position: absolute; left: 0; top: 44px; }
  .person { position: absolute; left: 37px; top: 62px; font-family: 'Roboto', sans-serif; }
  .person-name { font-size: 24px; font-weight: 500; line-height: 30px; }
  .person-name .first { color: var(--purple); }
  .person-name .last { color: var(--green); }
  .person-role { font-size: 16px; color: var(--ink); line-height: 22px; }
  .contacts {
    position: absolute; left: 37px; top: 242px;
    font-family: 'Roboto', sans-serif; font-size: 16px; color: var(--ink);
    list-style: none;
  }
  .contacts li { display: flex; align-items: center; height: 23.5px; }
  .contacts svg { width: 14px; height: 14px; margin-right: 18px; margin-left: 2px; }
  .contacts .postal { margin-top: 6px; }
  .back-brand {
    position: absolute; left: 356px; width: 260px; top: 270px;
    text-align: center;
    font-family: 'Comfortaa', sans-serif; font-weight: 400;
    font-size: 29px; line-height: 34px;
    color: var(--ink);
  }
</style>
</head>
<body>

<section class="card card-front">
  <h1 class="front-name">Tallowood<br>KinderMove</h1>
  <p class="front-tagline"><span class="rule"></span>Helping rural children and communities thrive<span class="rule"></span></p>
</section>

<section class="card card-back">
  <svg class="edge-accent" width="16" height="90" viewBox="0 0 16 90" aria-hidden="true">
    <defs>
      <linearGradient id="edgeGrad" x1="0" y1="0" x2="0" y2="1">
        <stop offset="0" stop-color="#5a1858"/>
        <stop offset="0.5" stop-color="#4d4d4d"/>
        <stop offset="1" stop-color="#23992b"/>
      </linearGradient>
    </defs>
    <path d="M0 0 Q16 45 0 90 Z" fill="url(#edgeGrad)"/>
  </svg>

  <div class="person">
    <p class="person-name"><span class="first">Mira</span> <span class="last">Toveland</span></p>
    <p class="person-role">Occupational Therapist</p>
  </div>

  <ul class="contacts">
    <li>
      <svg viewBox="0 0 16 16" aria-hidden="true"><path fill="#2a8f2f" d="M2 6c0-2 3-3 6-3s6 1 6 3v1h-3V6H5v1H2zM4 8h8l2 6H2z"/><circle cx="8" cy="11" r="1.6" fill="#efefef"/></svg>
      0487 552 019
    </li>
    <li>
      <svg viewBox="0 0 16 16" aria-hidden="true"><rect x="1" y="3" width="14" height="10" fill="#6a1b63"/><path d="M1 3l7 6 7-6M1 13l5-5M15 13l-5-5" stroke="#efefef" stroke-width="1.2" fill="none"/></svg>
      mira@tkmove.com.au
    </li>
    <li>
      <svg viewBox="0 0 16 16" aria-hidden="true"><circle cx="8" cy="8" r="7" fill="#2a8f2f"/><path d="M1 8h14M8 1v14M3 4.5h10M3 11.5h10" stroke="#efefef" stroke-width="0.9" fill="none"/><ellipse cx="8" cy="8" rx="3" ry="7" stroke="#efefef" stroke-width="0.9" fill="none"/></svg>
      www.tkmove.com.au
    </li>
    <li class="postal">PO Box 71 | BRELLAGUP WA 6388</li>
  </ul>

  <p class="back-brand">Tallowood<br>KinderMove</p>
</section>

</body>
</html>
```